Harborlane Consultants LLC web site

Harborlane Consultants LLC is a consulting and recruiting firm that provides education, perspective, guidance, and assistance to financial advisors. Dennis Malbrook is the founder of this new firm and is the only employee at this time.
Please see the attached overview which will provide much narrative describing the firm, its purpose, scope of services offered, and other useful information to help you design a web site.

Target Market(s)

US based financial advisors who are looking to transition their business to an independent ( non-employee ) business model.

Industry/Entity Type

Consultant

Coding

Coded - Design and coding required

Number of Pages Required

5+ page

Font styles to use
Sans Serif

Requirements
Must have
• all relevant pages for a basic web site : Home, About, Services offered, Contact, Resources , etc.
Nice to have
• color scheme : see logo in the attached briefing document

```html
<!DOCTYPE html>
<html lang="en">
<head>
<meta charset="utf-8">
<title>Harborlane Consultants LLC — Website Layouts</title>
<link href="https://fonts.googleapis.com/css2?family=Cinzel:wght@400;600&family=Lato:wght@300;400;700&display=swap" rel="stylesheet">
<style>
  :root{
    --navy:#1d4f7c;
    --navy-dark:#163b5c;
    --ink:#2b2b2b;
    --muted:#8a8a8a;
    --board:#ebebeb;
    --white:#ffffff;
    --band:#343638;
    --band-2:#2a2c2e;
    --sea-1:#1d3a45;
    --sea-2:#5d7a80;
    --sea-3:#a9b8b5;
    --rule:#dcdcdc;
  }
  *{box-sizing:border-box;margin:0;padding:0}
  html,body{width:1200px;height:2492px;overflow:hidden}
  body{position:relative;background:linear-gradient(var(--white) 0 400px,var(--board) 400px);font-family:'Lato',sans-serif;color:var(--ink)}
  .serif{font-family:'Cinzel',serif}

  /* brand lockup */
  .brand{position:absolute;top:52px;left:0;width:1200px;display:flex;justify-content:center;align-items:center;gap:18px}
  .brand-dot{width:56px;height:56px;border-radius:50%;background:var(--navy)}
  .brand-name{font-family:'Cinzel',serif;font-weight:600;font-size:44px;color:var(--navy);letter-spacing:3px}

  /* flat screen */
  .screen{position:absolute;left:300px;top:180px;width:600px;height:360px;background:var(--white);box-shadow:0 10px 30px rgba(0,0,0,.18);overflow:hidden}

  .nav{display:flex;align-items:center;justify-content:space-between;background:var(--white)}
  .nav-name{font-family:'Cinzel',serif;font-weight:600;color:var(--navy)}
  .nav-links{display:flex;align-items:center;color:var(--ink)}
  .nav-links .active{color:var(--navy);font-weight:700}
  .nav-btn{background:var(--navy);color:var(--white);text-transform:uppercase;letter-spacing:1px}

  .hero{position:relative;background:linear-gradient(180deg,var(--sea-1) 0%,var(--sea-2) 45%,var(--sea-3) 62%,var(--sea-1) 100%);display:flex;flex-direction:column;align-items:center;justify-content:center;color:var(--white);text-align:center}
  .hero-title{font-family:'Cinzel',serif;font-weight:400;letter-spacing:3px;line-height:1.05}
  .hero-sub{font-family:'Cinzel',serif;letter-spacing:3px}
  .hero-tag{font-weight:300;opacity:.9}

  .labels{position:absolute;top:840px;left:0;width:1200px;font-family:'Lato',sans-serif;font-weight:700;font-size:14px;letter-spacing:6px;color:var(--ink)}
  .labels span{position:absolute}

  /* desktop page */
  .desktop{position:absolute;left:148px;top:992px;width:760px;height:1436px;background:var(--white);box-shadow:0 6px 24px rgba(0,0,0,.12);overflow:hidden}
  .desktop .nav{height:56px;padding:0 40px}
  .desktop .nav-name{font-size:15px}
  .desktop .nav-links{gap:26px;font-size:10px}
  .desktop .nav-btn{font-size:9px;padding:8px 22px}
  .desktop .hero{height:172px}
  .desktop .hero-title{font-size:46px}
  .desktop .hero-sub{font-size:15px;margin-top:2px}
  .desktop .hero-tag{font-size:10px;margin-top:10px}

  .quote{text-align:center}
  .quote-mark{font-family:'Cinzel',serif;color:var(--navy)}
  .quote-text{font-style:italic;color:var(--ink);font-weight:300}
  .quote-by{color:var(--navy);text-transform:uppercase;letter-spacing:3px;font-weight:700}
  .desktop .quote{height:160px;padding:40px 140px 0}
  .desktop .quote-mark{font-size:34px;line-height:.8}
  .desktop .quote-text{font-size:13px;line-height:1.6;margin-top:6px}
  .desktop .quote-by{font-size:9px;margin-top:12px}

  .photo{background:radial-gradient(circle at 50% 48%,#6fa1b8 0 9%,#c9c2b4 10% 16%,#3a3936 17% 55%,#8a8780 56%,#c7c3bb 100%)}
  .desktop .photo-wrap{height:260px;display:flex;justify-content:center;align-items:center}
  .desktop .photo{width:340px;height:250px}

  .welcome-title{font-family:'Cinzel',serif;letter-spacing:3px;color:var(--ink)}
  .welcome-text{color:var(--muted);font-weight:300}
  .desktop .welcome{position:relative;height:300px;padding:38px 40px 0 300px}
  .desktop .welcome::before{content:"";position:absolute;left:-60px;top:60px;width:240px;height:240px;border-radius:50%;background:#f3f3f3}
  .desktop .welcome-title{position:relative;font-size:20px;text-align:right;display:flex;align-items:center;gap:14px}
  .desktop .welcome-title::before{content:"";flex:1;height:1px;background:var(--rule)}
  .desktop .welcome-text{position:relative;font-size:10px;line-height:1.7;margin-top:16px;text-align:right}

  .band{background:linear-gradient(100deg,var(--band) 0%,var(--band-2) 100%);color:var(--white);position:relative}
  .band-title{font-family:'Cinzel',serif;letter-spacing:3px;line-height:1.15}
  .band-text{color:#cfcfcf;font-weight:300}
  .band-btn{display:inline-block;background:var(--navy);color:var(--white);text-transform:uppercase;letter-spacing:1px}
  .desktop .band{margin-top:8px;height:232px;padding:36px 40px}
  .desktop .band-title{font-size:26px}
  .desktop .band-text{font-size:10px;line-height:1.6;margin-top:10px;width:330px}
  .desktop .band-btn{font-size:9px;padding:8px 22px;margin-top:16px}
  .desktop .band-circle{position:absolute;right:70px;top:40px;width:170px;height:170px;border-radius:50%;background:var(--navy)}

  .footer{background:var(--white)}
  .foot-name{font-family:'Cinzel',serif;font-weight:600;color:var(--navy)}
  .foot-links{list-style:none;color:var(--ink)}
  .foot-head{font-weight:700;text-transform:uppercase;letter-spacing:2px;color:var(--ink)}
  .contact-row{display:flex;align-items:flex-start;color:var(--muted)}
  .contact-icon{flex:none;border-radius:50%;background:var(--navy);display:flex;align-items:center;justify-content:center}
  .socials{display:flex}
  .social{border-radius:50%;background:var(--navy)}
  .legal{color:var(--muted);border-top:1px solid var(--rule)}

  .desktop .footer{height:248px;padding:24px 40px 0;position:relative}
  .desktop .foot-grid{display:flex;gap:150px}
  .desktop .foot-name{font-size:13px}
  .desktop .foot-links{font-size:10px;line-height:1.9;margin-top:10px}
  .desktop .foot-head{font-size:9px;margin-bottom:10px}
  .desktop .contact-row{gap:10px;font-size:9px;line-height:1.5;margin-bottom:8px}
  .desktop .contact-icon{width:16px;height:16px}
  .desktop .socials{gap:10px;margin-top:12px}
  .desktop .social{width:12px;height:12px}
  .desktop .legal{position:absolute;left:40px;right:40px;bottom:14px;padding-top:8px;font-size:8px;display:flex;justify-content:center;gap:30px}

  /* mobile page */
  .mobile{position:absolute;left:988px;top:992px;width:120px;height:1436px;background:var(--white);box-shadow:0 6px 24px rgba(0,0,0,.12);overflow:hidden}
  .mobile .nav{height:32px;padding:0 8px}
  .mobile .nav-name{font-size:6px}
  .mobile .burger{width:12px;height:9px;border-top:2px solid var(--navy);border-bottom:2px solid var(--navy);position:relative}
  .mobile .burger::after{content:"";position:absolute;left:0;right:0;top:1.5px;height:2px;background:var(--navy)}
  .mobile .hero{height:136px;padding:0 6px}
  .mobile .hero-title{font-size:13px;letter-spacing:1px}
  .mobile .hero-sub{font-size:6px;letter-spacing:1px}
  .mobile .quote{height:120px;padding:16px 10px 0}
  .mobile .quote-mark{font-size:16px}
  .mobile .quote-text{font-size:6px;line-height:1.6}
  .mobile .quote-by{font-size:4.5px;margin-top:6px;letter-spacing:1px}
  .mobile .photo{height:140px;margin:0 10px}
  .mobile .welcome{height:340px;padding:22px 10px 0;text-align:right}
  .mobile .welcome-title{font-size:8px;letter-spacing:1px;line-height:1.4}
  .mobile .welcome-text{font-size:5px;line-height:1.7;margin-top:10px}
  .mobile .band{margin-top:20px;height:220px;padding:18px 8px}
  .mobile .band-title{font-size:8px;letter-spacing:1px}
  .mobile .band-text{font-size:5px;line-height:1.6;margin-top:8px}
  .mobile .band-btn{font-size:4.5px;padding:4px 8px;margin-top:10px}
  .mobile .band-circle{position:absolute;right:8px;bottom:14px;width:50px;height:50px;border-radius:50%;background:var(--navy)}
  .mobile .footer{padding:20px 8px 0;height:428px;position:relative}
  .mobile .foot-name{font-size:6px}
  .mobile .foot-links{font-size:6px;line-height:2;margin-top:10px}
  .mobile .foot-head{font-size:5px;margin:18px 0 8px}
  .mobile .contact-row{gap:5px;font-size:5px;line-height:1.5;margin-bottom:8px}
  .mobile .contact-icon{width:9px;height:9px}
  .mobile .socials{gap:6px;margin-top:10px}
  .mobile .social{width:8px;height:8px}
  .mobile .legal{position:absolute;left:8px;right:8px;bottom:14px;padding-top:6px;font-size:4.5px;text-align:center;line-height:1.6}

  /* screen-scale */
  .screen .nav{height:24px;padding:0 22px}
  .screen .nav-name{font-size:8px}
  .screen .nav-links{gap:14px;font-size:5.5px}
  .screen .nav-btn{font-size:5px;padding:4px 12px}
  .screen .hero{height:336px}
  .screen .hero-title{font-size:46px}
  .screen .hero-sub{font-size:14px}
  .screen .hero-tag{font-size:8px;margin-top:10px}
</style>
</head>
<body>

<header class="brand">
  <span class="brand-dot" aria-hidden="true"></span>
  <span class="brand-name">HARBORLANE CONSULTANTS LLC</span>
</header>

<section class="screen" aria-label="Home page preview">
  <nav class="nav">
    <span class="nav-name">HARBORLANE</span>
    <div class="nav-links"><span class="active">Home</span><span>About</span><span>Services</span><span>Resources</span><span class="nav-btn">Contact Us</span></div>
  </nav>
  <div class="hero" role="img" aria-label="Photograph of a lone figure in a small boat on a stormy sea under a lighthouse beam">
    <h1 class="hero-title">HARBORLANE</h1>
    <p class="hero-sub">CONSULTANTS LLC</p>
    <p class="hero-tag">Guiding advisors toward an independent future</p>
  </div>
</section>

<div class="labels"><span style="left:462px">DESKTOP</span><span style="left:1012px">MOBILE</span></div>

<main class="desktop">
  <nav class="nav">
    <span class="nav-name">HARBORLANE</span>
    <div class="nav-links"><span class="active">Home</span><span>About</span><span>Services Offered</span><span>Resources</span><span class="nav-btn">Contact Us</span></div>
  </nav>
  <div class="hero" role="img" aria-label="Photograph of a lone figure in a small boat on a stormy sea">
    <h1 class="hero-title">HARBORLANE</h1>
    <p class="hero-sub">CONSULTANTS LLC</p>
    <p class="hero-tag">Education, perspective and guidance for financial advisors</p>
  </div>
  <section class="quote">
    <div class="quote-mark">“</div>
    <p class="quote-text">The pessimist complains about the wind; the optimist expects it to change; the realist adjusts the sails.</p>
    <p class="quote-by">Arthur Wenlock</p>
  </section>
  <div class="photo-wrap"><div class="photo" role="img" aria-label="Photograph of a compass resting on a dark leather notebook"></div></div>
  <section class="welcome">
    <h2 class="welcome-title">WELCOME TO HARBORLANE</h2>
    <p class="welcome-text">Harborlane Consultants LLC provides education, perspective, guidance and assistance to financial advisors considering a move to an independent business model. We help you weigh your options with clarity and confidence.</p>
    <p class="welcome-text">Founded by Dennis Malbrook, the firm brings decades of industry experience to every conversation, offering honest counsel at each stage of your transition, from first questions to your first day as an owner.</p>
    <p class="welcome-text">Whether you are exploring or ready to move, we are here to help you chart the course.</p>
  </section>
  <section class="band">
    <h2 class="band-title">I'M WORKING WITH<br>HARBORLANE</h2>
    <p class="band-text">Already partnering with us? Find resources, checklists and next steps to keep your transition moving forward smoothly.</p>
    <span class="band-btn">Learn More</span>
    <span class="band-circle" aria-hidden="true"></span>
  </section>
  <footer class="footer">
    <div class="foot-grid">
      <div>
        <span class="foot-name">HARBORLANE</span>
        <ul class="foot-links"><li>Home</li><li>About</li><li>Services Offered</li><li>Resources</li><li>Contact</li></ul>
        <div class="socials"><span class="social"></span><span class="social"></span><span class="social"></span></div>
      </div>
      <div>
        <p class="foot-head">Contact Info</p>
        <div class="contact-row"><span class="contact-icon"><svg width="8" height="8" viewBox="0 0 10 10"><path d="M5 1a3 3 0 0 1 3 3c0 2-3 5-3 5S2 6 2 4a3 3 0 0 1 3-3z" fill="#fff"/></svg></span><span>Dennis Malbrook, Founder<br>120 Harbor Street, Suite 4, Anytown, USA</span></div>
        <div class="contact-row"><span class="contact-icon"><svg width="8" height="8" viewBox="0 0 10 10"><path d="M2 1h2l1 2-1 1a5 5 0 0 0 2 2l1-1 2 1v2a1 1 0 0 1-1 1A7 7 0 0 1 1 2a1 1 0 0 1 1-1z" fill="#fff"/></svg></span><span>(555) 201-4488</span></div>
        <div class="contact-row"><span class="contact-icon"><svg width="8" height="8" viewBox="0 0 10 10"><rect x="1" y="2" width="8" height="6" fill="none" stroke="#fff"/><path d="M1 2l4 3 4-3" fill="none" stroke="#fff"/></svg></span><span>hello@harborlane.example</span></div>
      </div>
    </div>
    <div class="legal"><span>© Harborlane Consultants LLC</span><span>Privacy Policy</span><span>Terms of Use</span></div>
  </footer>
</main>

<aside class="mobile">
  <nav class="nav"><span class="nav-name">HARBORLANE</span><span class="burger" aria-hidden="true"></span></nav>
  <div class="hero" role="img" aria-label="Photograph of a lone figure in a small boat on a stormy sea">
    <h1 class="hero-title">HARBORLANE</h1>
    <p class="hero-sub">CONSULTANTS LLC</p>
  </div>
  <section class="quote">
    <div class="quote-mark">“</div>
    <p class="quote-text">The realist adjusts the sails and keeps moving forward.</p>
    <p class="quote-by">Arthur Wenlock</p>
  </section>
  <div class="photo" role="img" aria-label="Photograph of a compass on a notebook"></div>
  <section class="welcome">
    <h2 class="welcome-title">WELCOME TO<br>HARBORLANE</h2>
    <p class="welcome-text">We guide financial advisors toward an independent business model with education, perspective and practical help.</p>
    <p class="welcome-text">Founded by Dennis Malbrook, the firm offers honest counsel at every stage of your move.</p>
    <p class="welcome-text">Explore your options and chart your course with us.</p>
  </section>
  <section class="band">
    <h2 class="band-title">I'M WORKING WITH<br>HARBORLANE</h2>
    <p class="band-text">Find resources and next steps for your transition.</p>
    <span class="band-btn">Learn More</span>
    <span class="band-circle" aria-hidden="true"></span>
  </section>
  <footer class="footer">
    <span class="foot-name">HARBORLANE</span>
    <ul class="foot-links"><li>Home</li><li>About</li><li>Services</li><li>Resources</li><li>Contact</li></ul>
    <p class="foot-head">Contact Info</p>
    <div class="contact-row"><span class="contact-icon"></span><span>120 Harbor Street, Anytown</span></div>
    <div class="contact-row"><span class="contact-icon"></span><span>(555) 201-4488</span></div>
    <div class="contact-row"><span class="contact-icon"></span><span>hello@harborlane.example</span></div>
    <div class="socials"><span class="social"></span><span class="social"></span><span class="social"></span></div>
    <div class="legal">© Harborlane Consultants LLC<br>Privacy · Terms</div>
  </footer>
</aside>

</body>
</html>
```